Redo a PPT pres. - Real Estate in Brazil - Socially equitable investments in Social Housing

We need to redo the presentation attached. It is an institutional presentation to attract local and foreign investors to invest in Brazilian Social Housing Projects structured by our company "TRV".
A middle class of 100 million, a housing deficit of 9M, a strong political will & positive income generation trends constitute grounds for a significant demand in social housing.
This make a perfect scheme for investors to invest in Brazilian Social Housing.
"TRV", is a consulting "boutique" focused in Brazilian real estate, specialized in structuring, analyzing and originating Brazilian social housing projects.
TRV is part of the group TRQ. TRQ is structured to create value through each step of the residential real estate business - structuring, financing, sales, marketing and technology.
We would like to see designs that use mainly the color blue. The final design should communicate financial safety and professionalism. In order to reach our needs, the designer will need to have basic understanding of finance and investment in order to highlight the most important information.
The idea is to receive back the PPT with each page redesigned and an homogeneous identity.
To all designers,
Target Market(s)
Institutional Investors and wealthy individuals
Industry/Entity Type
Residential
Look and feel
Each slider illustrates characteristics of the customer's brand and the style your logo design should communicate.

```html
<!DOCTYPE html>
<html lang="en">
<head>
<meta charset="utf-8">
<title>TRV – Social Housing in Brazil</title>
<link href="https://fonts.googleapis.com/css2?family=Caladea:ital,wght@0,400;0,700;1,400&family=PT+Sans:wght@400;700&display=swap" rel="stylesheet">
<style>
:root{
  --stage:#ececec;
  --paper:#ffffff;
  --paper-shade:#eef1f5;
  --blue-deep:#1b4a8c;
  --blue-mid:#2467b3;
  --blue-bright:#2b8fd4;
  --cyan:#3aa6dc;
  --ink:#333a44;
  --ink-soft:#6a717b;
  --serif:'Caladea', Georgia, serif;
  --sans:'PT Sans', Arial, sans-serif;
}
*{box-sizing:border-box;margin:0;padding:0}
html,body{width:1200px;height:648px;overflow:hidden}
body{background:var(--stage);position:relative;font-family:var(--sans);color:var(--ink)}
.slide{position:absolute;width:308px;height:229px;background:linear-gradient(180deg,var(--paper) 70%,var(--paper-shade));box-shadow:0 2px 6px rgba(0,0,0,.25);overflow:hidden}
.s1{left:97px;top:63px}.s2{left:443px;top:63px}.s3{left:785px;top:63px}
.s4{left:83px;top:352px}.s5{left:436px;top:352px}.s6{left:789px;top:352px}
.slide-title{position:absolute;left:14px;top:8px;font-family:var(--serif);font-weight:700;color:var(--blue-mid);font-size:14px;white-space:nowrap}
.slide-sub{position:absolute;left:14px;top:30px;font-size:9.5px;color:var(--ink-soft);width:280px;line-height:1.25}
.page-mark{position:absolute;right:8px;bottom:6px;text-align:right;font-family:var(--serif);color:var(--blue-deep);line-height:1}
.page-mark .num{display:block;font-size:16px;color:var(--blue-bright)}
.page-mark .brand{font-size:10px}
.brand-name{font-family:var(--serif);color:var(--blue-deep);font-weight:400}
.houses-art{position:absolute;background:linear-gradient(160deg,#ffffff 0%,#cfe4f5 35%,#3a9ad8 70%,#1b4a8c 100%)}
/* slide 1 */
.s1 .brand-name{position:absolute;right:22px;top:8px;font-size:30px}
.s1 .cover-title{position:absolute;right:14px;top:44px;font-family:var(--serif);font-weight:400;font-size:22px;color:var(--blue-deep);white-space:nowrap}
.s1 .cover-tag{position:absolute;right:12px;top:72px;font-family:var(--serif);font-size:11.5px;color:var(--cyan);white-space:nowrap}
.s1 .houses-art{left:0;top:110px;width:308px;height:119px;clip-path:polygon(0 0,45% 10%,100% 40%,100% 100%,0 100%)}
/* slide 2 */
.diagram{position:absolute;left:0;top:0;width:308px;height:229px}
.pill{position:absolute;background:linear-gradient(180deg,#4fa7e6,#1f5fae);color:#fff;font-size:6px;font-weight:700;text-align:center;border-radius:8px;padding:3px 4px;line-height:1.2;box-shadow:0 1px 2px rgba(0,0,0,.35)}
/* slide 3 */
.agenda{position:absolute;left:18px;top:32px;list-style:none;font-size:6.8px;font-weight:700;color:var(--ink);line-height:14px}
.agenda li::before{content:"";display:inline-block;width:4px;height:4px;background:var(--blue-bright);border-radius:50%;margin-right:5px;vertical-align:middle}
.section-head{position:absolute;left:18px;top:136px;font-family:var(--serif);font-weight:700;font-size:12.5px;color:var(--blue-mid);border-bottom:1.5px solid var(--blue-deep);padding-bottom:1px;white-space:nowrap}
.green-light{position:absolute;left:16px;top:172px;width:150px;height:34px;border-radius:17px;background:linear-gradient(180deg,#5fb2ec,#1d5aa8);color:#fff;font-family:var(--serif);font-weight:700;font-size:15px;line-height:34px;padding-left:22px;box-shadow:0 3px 5px rgba(0,0,0,.3)}
.green-light .badge{position:absolute;right:0;top:0;width:34px;height:34px;border-radius:50%;background:#fff;border:2px solid var(--blue-deep);color:var(--blue-deep);text-align:center;line-height:30px;font-size:17px}
/* slide 4 & 5 panels */
.panel{position:absolute;background:#fff;border-radius:6px;box-shadow:0 1px 4px rgba(0,0,0,.3);font-size:4.6px;line-height:1.35;color:var(--ink-soft);padding:20px 6px 6px}
.panel h3{position:absolute;left:8px;right:8px;top:-4px;height:15px;border-radius:8px;background:linear-gradient(180deg,#4fa7e6,#1f5fae);color:#fff;font-family:var(--serif);font-size:7.5px;text-align:center;line-height:15px;white-space:nowrap;overflow:hidden}
.panel p{margin-bottom:3px}
.panel b{color:var(--blue-deep)}
.charts{position:absolute;left:14px;top:56px;width:120px;height:165px}
.s5 .panel{font-size:5px}
/* slide 6 */
.s6 .brand-name{position:absolute;right:26px;top:10px;font-size:30px}
.s6 .thanks{position:absolute;right:14px;top:46px;font-family:var(--serif);font-weight:400;font-size:30px;color:var(--blue-bright);white-space:nowrap}
.s6 .thanks-sub{position:absolute;right:14px;top:82px;font-family:var(--serif);font-size:14px;color:#111}
.s6 .houses-art{left:0;top:100px;width:308px;height:129px;clip-path:polygon(0 10%,40% 0,100% 45%,100% 100%,0 100%)}
</style>
</head>
<body>

<section class="slide s1">
  <span class="brand-name">TRV</span>
  <h1 class="cover-title">Social housing in brazil</h1>
  <p class="cover-tag">High Yield Return For A Quasi Sovereign Risk</p>
  <div class="houses-art" role="img" aria-label="Illustration of outlined houses over flowing blue waves"></div>
</section>

<section class="slide s2">
  <h2 class="slide-title">How To Invest In Social Housing In Brazil?</h2>
  <p class="slide-sub">A socially conscious &amp; lucrative investment</p>
  <svg class="diagram" viewBox="0 0 308 229">
    <ellipse cx="154" cy="134" rx="84" ry="76" fill="none" stroke="#9aa4b0" stroke-width="1"/>
  </svg>
  <div class="pill" style="left:108px;top:50px;width:92px">Building housing units for low to middle-class buyers</div>
  <div class="pill" style="left:58px;top:90px;width:72px">Target IRR<br>25-30%</div>
  <div class="pill" style="left:176px;top:90px;width:74px">Investing in individual Projects</div>
  <div class="pill" style="left:42px;top:124px;width:68px">Time Horizon<br>3-4 Years</div>
  <div class="pill" style="left:192px;top:124px;width:80px">Management<br>Specialized International &amp; local team</div>
  <div class="pill" style="left:56px;top:158px;width:78px">Equity participation of<br>R$2-10 millions</div>
  <div class="pill" style="left:176px;top:158px;width:78px">Co-investing with local mid-size developers</div>
  <div class="pill" style="left:108px;top:194px;width:92px;padding:6px 4px">Co-financed by government</div>
  <div class="page-mark"><span class="num">2</span><span class="brand">TRV</span></div>
</section>

<section class="slide s3">
  <h2 class="slide-title">The Time Is Now!</h2>
  <ul class="agenda">
    <li>Macro-environment &amp; Mortgage market: Green Light</li>
    <li>A sophisticated &amp; successful program: Catalyst</li>
    <li>Investment Structure of a typical project: Leverage &amp; Limited Risks</li>
    <li>Small &amp; mid size developers: A partner by choice</li>
    <li>TRV: Value added &amp; Risk mitigation</li>
    <li>TRQ: TRV, part of an integrated family of companies</li>
    <li>Appendix: Next step…TRV Fund (2013)</li>
  </ul>
  <h3 class="section-head">Macro-environment &amp; Mortgage Market</h3>
  <div class="green-light">Green Light<span class="badge">1</span></div>
  <div class="page-mark"><span class="num">3</span><span class="brand">TRV</span></div>
</section>

<section class="slide s4">
  <h2 class="slide-title">A Middle Class Of 100 Million People…</h2>
  <p class="slide-sub">Strong political will &amp; positive income generation trends constitute grounds for a significant demand in social housing</p>
  <div class="panel" style="left:14px;top:72px;width:136px;height:148px">
    <h3>Politics</h3>
    <p>Brazil launched a fierce battle against poverty 10 years ago with President Moreau. The positive economic environment has helped implement these policies.</p>
    <p><b>National Growth Plan (2007-10): R$480B</b><br>- Public investments in infrastructure<br>- Lighten the administrative and legal burden on private initiatives<br>- Stimulating Credit &amp; Financing for the real estate sector</p>
    <p><b>National Growth Plan (2011-14): R$960B</b><br>- Better City &amp; Community: R$90B<br>- Water, Light, Transportation: R$130B<br>- Energy: R$460B<br>- <b>Housing: R$278B</b> – public financing and subsidies through various programs, notably <b>Casa Nova Brasil (CNB)</b> for low and middle classes and <b>Lar Conjunto</b></p>
  </div>
  <div class="panel" style="left:160px;top:72px;width:134px;height:112px">
    <h3>Emergence Of The Middle Class</h3>
    <p>- It reached remarkable success: poverty has decreased from 39% of population in 1999 to less than 20% in 2012</p>
    <p>- More than 40M people have recently entered the middle class. They need decent housing</p>
    <p><b>Middle class will represent 54% of the population</b> by the end of 2012 (overall population of 197M). Constitution of an upper middle class with an appetite for pricier products</p>
    <p><b>Housing deficit is estimated to be around 9M</b> of which 7M in urban housing</p>
  </div>
  <div class="page-mark"><span class="num">4</span><span class="brand">TRV</span></div>
</section>

<section class="slide s5">
  <h2 class="slide-title">…and Still Growing</h2>
  <p class="slide-sub">Positive demographics &amp; economic environment will sustain the demanda</p>
  <svg class="charts" viewBox="0 0 120 165" role="presentation">
    <g fill="#2b5fa3">
      <rect x="8" y="20" width="5" height="26"/><rect x="16" y="18" width="5" height="28"/><rect x="24" y="22" width="5" height="24"/><rect x="32" y="16" width="5" height="30"/><rect x="40" y="19" width="5" height="27"/><rect x="48" y="21" width="5" height="25"/><rect x="56" y="24" width="5" height="22"/><rect x="64" y="18" width="5" height="28"/>
    </g>
    <polyline points="8,4 20,8 32,12 44,14 56,20 68,24" fill="none" stroke="#d23b2f" stroke-width="1.2"/>
    <line x1="6" y1="46" x2="72" y2="46" stroke="#999" stroke-width=".5"/>
    <g fill="#2b5fa3">
      <rect x="12" y="62" width="54" height="3"/><rect x="12" y="70" width="48" height="3"/><rect x="12" y="78" width="44" height="3"/><rect x="12" y="86" width="40" height="3"/><rect x="12" y="94" width="36" height="3"/><rect x="12" y="102" width="30" height="3"/>
    </g>
    <g fill="#d23b2f">
      <rect x="12" y="65" width="50" height="2"/><rect x="12" y="73" width="46" height="2"/><rect x="12" y="81" width="40" height="2"/><rect x="12" y="89" width="38" height="2"/><rect x="12" y="97" width="32" height="2"/><rect x="12" y="105" width="28" height="2"/>
    </g>
    <g>
      <rect x="14" y="132" width="8" height="12" fill="#4aa3d8"/><rect x="14" y="124" width="8" height="8" fill="#d23b2f"/><rect x="14" y="118" width="8" height="6" fill="#6ab04c"/><rect x="14" y="144" width="8" height="5" fill="#7b4fa0"/>
      <rect x="28" y="130" width="8" height="14" fill="#4aa3d8"/><rect x="28" y="120" width="8" height="10" fill="#d23b2f"/><rect x="28" y="115" width="8" height="5" fill="#6ab04c"/><rect x="28" y="144" width="8" height="5" fill="#7b4fa0"/>
      <rect x="42" y="128" width="8" height="16" fill="#4aa3d8"/><rect x="42" y="118" width="8" height="10" fill="#d23b2f"/><rect x="42" y="113" width="8" height="5" fill="#6ab04c"/><rect x="42" y="144" width="8" height="5" fill="#7b4fa0"/>
    </g>
    <line x1="10" y1="149" x2="56" y2="149" stroke="#999" stroke-width=".5"/>
  </svg>
  <div class="panel" style="left:150px;top:70px;width:144px;height:110px">
    <h3>End-buyers</h3>
    <p>- Aging population: <b>Average number of persons per household</b> shrunk from 3.7 in 1991 to 3.1 in 2010. Expected to remain around 3</p>
    <p>- Projection of <b>12M more people by 2020</b></p>
    <p>- <b>Natural increase in number of households / housing demand</b></p>
    <p>- <b>Considerable growth in real wages</b>, average <b>5.3%</b> from 2003-2012</p>
    <p><b>-20M more people will have entered Class C from 2008 to 2014</b></p>
  </div>
  <div class="page-mark"><span class="num">5</span><span class="brand">TRV</span></div>
</section>

<section class="slide s6">
  <span class="brand-name">TRV</span>
  <h2 class="thanks">Thank You!</h2>
  <p class="thanks-sub">for watching!</p>
  <div class="houses-art" role="img" aria-label="Illustration of outlined houses over flowing blue waves"></div>
</section>

</body>
</html>
```